Local business providing residential house cleaning services

We need a business card design that is "cute" or "cartoonish" while still maintaining a professional appeal. Tidy Nook Cleaners is the name. We would like to use a "pin up girl" or maid next to the name with a broom or vacuum cleaner. We want the look to have a 50's American look to it. We are not sure if we want the pin up girl in a maid outfit or with a broom or vacuum cleaner but we hope some of you will be able to take these ideas and be creative. If you have any questions at all please don't hesitate to message me so that we can get the best design possible. Thank you very much and I look forward to seeing some designs! Mira Delgado

Target Market(s)

Upper class Americans that are busy and have money and want to come home to a clean house.

Industry/Entity Type

Cleaning Service

Contact Information for Business Card

Pin up girl incorporated into the card is a must.

Font styles to use
Decorative
Script

Requirements
Must have
• Pin up girl
Nice to have
• A crown used on the Q possibly.

```html
<!DOCTYPE html>
<html lang="en">
<head>
<meta charset="utf-8">
<title>Tidy Nook Cleaners – Business Card</title>
<link rel="stylesheet" href="https://fonts.googleapis.com/css2?family=Roboto:wght@400;500;700&display=swap">
<style>
  :root {
    --backdrop: #e4e1da;
    --card-dark: #2b2a28;
    --card-cream: #f7e9c9;
    --gold: #d6a419;
    --gold-light: #f6df7e;
    --ink: #2a2a2a;
    --art-tone: #4a4844;
    --art-tone-light: #5c5a55;
  }
  * { margin: 0; padding: 0; box-sizing: border-box; }
  html, body {
    width: 1200px;
    height: 925px;
    overflow: hidden;
    background: var(--backdrop);
    font-family: "Roboto", Arial, sans-serif;
  }
  .business-card {
    position: absolute;
    left: 50px;
    top: 123px;
    width: 1100px;
    height: 678px;
    background: var(--card-cream);
    box-shadow: 0 6px 18px rgba(0, 0, 0, 0.18);
    overflow: hidden;
  }
  .brand-panel {
    position: absolute;
    left: 0;
    top: 0;
    width: 100%;
    height: 409px;
    background: var(--card-dark);
  }
  .pinup-art {
    position: absolute;
    left: 364px;
    top: 39px;
    width: 431px;
    height: 236px;
    border-radius: 10px;
    background: linear-gradient(135deg, var(--art-tone-light), var(--art-tone));
  }
  .brand-name {
    position: absolute;
    left: 0;
    top: 288px;
    width: 100%;
    text-align: center;
    color: var(--gold);
    font-weight: 700;
    font-size: 60px;
    line-height: 72px;
    letter-spacing: 0.5px;
  }
  .gold-rule {
    position: absolute;
    left: 0;
    top: 409px;
    width: 100%;
    height: 10px;
    background: linear-gradient(90deg, var(--gold) 0%, var(--gold) 55%, var(--gold-light) 80%, var(--gold) 100%);
  }
  .contact-panel {
    position: absolute;
    left: 0;
    top: 419px;
    width: 100%;
    height: 259px;
  }
  .person-name {
    position: absolute;
    top: 48px;
    width: 100%;
    text-align: center;
    color: var(--ink);
    font-weight: 500;
    font-size: 33px;
  }
  .contact-row {
    position: absolute;
    top: 144px;
    width: 100%;
    display: flex;
    justify-content: center;
    gap: 48px;
    color: var(--ink);
    font-size: 29px;
  }
  .contact-item {
    display: flex;
    align-items: center;
    gap: 14px;
  }
  .contact-icon { width: 30px; height: 30px; fill: var(--ink); }
</style>
</head>
<body>
  <main class="business-card">
    <section class="brand-panel">
      <div class="pinup-art" role="img" aria-label="Illustration of a 1950s pin-up maid vacuuming the floor"></div>
      <h1 class="brand-name">Tidy Nook Cleaners</h1>
    </section>
    <div class="gold-rule"></div>
    <section class="contact-panel">
      <p class="person-name">Mira Delgado</p>
      <div class="contact-row">
        <span class="contact-item">
          <svg class="contact-icon" viewBox="0 0 24 24" aria-hidden="true">
            <path d="M6.6 2.2c.5-.3 1.1-.2 1.5.3l2.3 3.3c.3.5.3 1.1-.1 1.5L8.8 8.8c.9 2.5 2.9 4.8 5.3 6.2l1.5-1.4c.4-.4 1-.4 1.5-.1l3.3 2.2c.5.3.6 1 .3 1.5l-1.4 2.3c-.5.8-1.5 1.2-2.4.9C9.8 18.4 5.2 12.8 4.2 5.6c-.1-.9.3-1.8 1.1-2.3z"/>
          </svg>
          <span>555-214-0937</span>
        </span>
        <span class="contact-item">
          <svg class="contact-icon" viewBox="0 0 24 24" aria-hidden="true">
            <path d="M2 5h20v14H2z M3.6 6.5v.4L12 12.6l8.4-5.7v-.4z M3.6 8.8v8.7h16.8V8.8L12 14.5z" fill-rule="evenodd"/>
          </svg>
          <span>mira.tidynook@mailbox.test</span>
        </span>
      </div>
    </section>
  </main>
</body>
</html>
```